SilverLedgerOak - Double Sided Business Card

We are looking for design options or our business cards. We are a Business Solutions and HR solutions Provider - the theme is business, for this card.

Our brand colours are represented within our logo.

Details needed to be put on the front of the business card are:

Employees name: [Sample Name]
Role: [Sample Role]

Address: Suite 4 - Level 3/48 Halloran Avenue Parramatta NSW 2150
M: 0000 000 000
P: 1300 847 213
F: 1300 847 286
E: sample@silverledgeroak.com.au
www.silverledgeroak.com.au
Updates

Reason: Hello, could we please increase our deadline by 5 days. Thanking you, Tess

Target Market(s)

Business Owners, also Candidates looking for Employment

Industry/Entity Type

Business

Contact Information for Business Card

Role: [Sample Role]

M: 0000 000 000
P: 1300 847 213
F: 1300 847 286

Font styles to use
Sans Serif

Colors
3276b5
3176b5
0455a3
85abd2
cfdeed
ffffff
000000
1b1b1b
757575

Requirements
Must have
• Details needed to be put on the front of the business card are:
• Employees name: [Sample Name]
• Role: [Sample Role]
• Address: Suite 4 - Level 3/48 Halloran Avenue Parramatta NSW 2150
• M: 0000 000 000
• P: 1300 847 213
• F: 1300 847 286
• E: sample@silverledgeroak.com.au
• www.silverledgeroak.com.au
Nice to have
• Simplicity, clean and professional.

```html
<!DOCTYPE html>
<html lang="en">
<head>
<meta charset="utf-8">
<title>SilverLedgerOak Business Card</title>
<link href="https://fonts.googleapis.com/css2?family=Michroma&family=Roboto:wght@400;700&display=swap" rel="stylesheet">
<style>
  :root {
    --page-bg: #3a3a3a;
    --navy: #12294a;
    --white: #ffffff;
    --brand-blue: #0455a3;
    --mid-blue: #3276b5;
    --light-blue: #85abd2;
    --ink: #1b1b1b;
    --grey: #757575;
  }
  * { margin: 0; padding: 0; box-sizing: border-box; }
  html, body { width: 1200px; height: 900px; overflow: hidden; }
  body {
    background: var(--page-bg);
    font-family: "Roboto", Arial, sans-serif;
    position: relative;
  }
  .card {
    position: absolute;
    width: 660px;
    height: 378px;
    border-radius: 26px;
    overflow: hidden;
  }
  .card--back { left: 440px; top: 50px; background: var(--white); }
  .card--front { left: 100px; top: 470px; background: var(--navy); color: var(--white); }

  /* brand lockup */
  .brand { display: flex; align-items: center; gap: 12px; }
  .brand__square { width: 38px; height: 38px; border: 4px solid currentColor; }
  .brand__name { font-family: "Roboto", Arial, sans-serif; font-weight: 700; font-size: 32px; letter-spacing: 0.5px; }
  .tagline {
    font-size: 10.5px; font-weight: 700; padding-top: 6px; margin-top: 8px;
    border-top: 1px solid currentColor;
  }

  /* back side */
  .back-lockup {
    position: absolute; left: 0; right: 0; top: 110px;
    display: flex; flex-direction: column; align-items: center;
  }
  .back-lockup .brand { color: var(--brand-blue); }
  .back-lockup .tagline { color: var(--ink); border-top-color: var(--navy); }
  .website {
    margin-top: 26px; font-weight: 700; font-size: 14px; letter-spacing: 1px;
    color: var(--navy);
  }

  /* front side */
  .front-lockup { position: absolute; left: 40px; top: 36px; color: var(--white); }
  .front-lockup .tagline { border-top-color: var(--light-blue); }
  .phones { position: absolute; left: 40px; top: 150px; }
  .contact-line { display: flex; align-items: center; gap: 12px; font-size: 19px; margin-bottom: 8px; }
  .contact-icon { width: 24px; height: 24px; flex: none; }
  .person { position: absolute; right: 40px; top: 150px; text-align: right; }
  .person__name { font-family: "Michroma", Arial, sans-serif; font-size: 20px; letter-spacing: 1px; }
  .person__role { font-family: "Michroma", Arial, sans-serif; font-size: 13px; color: var(--light-blue); letter-spacing: 1.5px; margin-top: 4px; }
  .divider { position: absolute; left: 40px; right: 40px; top: 225px; height: 1px; background: var(--light-blue); }
  .office-lines { position: absolute; left: 370px; top: 248px; }
  .address { position: absolute; left: 40px; bottom: 34px; font-size: 17px; }
</style>
</head>
<body>

<section class="card card--back" aria-label="Card back">
  <div class="back-lockup">
    <div class="brand">
      <span class="brand__square"></span>
      <span class="brand__name">SilverLedgerOak</span>
    </div>
    <p class="tagline">Guiding growing firms and teams towards lasting results</p>
    <p class="website">WWW.SLOAKPF.COM</p>
  </div>
</section>

<section class="card card--front" aria-label="Card front">
  <div class="front-lockup">
    <div class="brand">
      <span class="brand__square"></span>
      <span class="brand__name">SilverLedgerOak</span>
    </div>
    <p class="tagline">Guiding growing firms and teams towards lasting results</p>
  </div>

  <div class="phones">
    <p class="contact-line">
      <svg class="contact-icon" viewBox="0 0 24 24" fill="none" stroke="#85abd2" stroke-width="1.5"><circle cx="12" cy="12" r="11"/><rect x="9" y="6" width="6" height="12" rx="1"/></svg>
      700.418.3957
    </p>
    <p class="contact-line">
      <svg class="contact-icon" viewBox="0 0 24 24" fill="none" stroke="#85abd2" stroke-width="1.5"><circle cx="12" cy="12" r="11"/><path d="M7 10c0-2 10-2 10 0v1h-3v-1h-4v1H7z M8 12h8l1 5H7z"/></svg>
      801.364.7120
    </p>
  </div>

  <div class="person">
    <p class="person__name">DANIEL ASHWORTH</p>
    <p class="person__role">MANAGING DIRECTOR</p>
  </div>

  <div class="divider"></div>

  <div class="office-lines">
    <p class="contact-line">
      <svg class="contact-icon" viewBox="0 0 24 24" fill="none" stroke="#85abd2" stroke-width="1.5"><circle cx="12" cy="12" r="11"/><rect x="7" y="10" width="10" height="6"/><rect x="9" y="7" width="6" height="3"/></svg>
      801.526.4418
    </p>
    <p class="contact-line">
      <svg class="contact-icon" viewBox="0 0 24 24" fill="none" stroke="#85abd2" stroke-width="1.5"><circle cx="12" cy="12" r="11"/><rect x="6.5" y="8" width="11" height="8"/><path d="M6.5 8l5.5 4.5L17.5 8"/></svg>
      Daniel@ledgermail.net
    </p>
  </div>

  <p class="address">Suite 4 - Level 3/48 Halloran Avenue, Kellsbrook NSW 2163</p>
</section>

</body>
</html>
```